Business Card Design needed for logo design project

Our 2-sided business card needs to include the information sent to the awarded winner.

Reason: So sorry for the delay. Many pressing deadlines in this week.

Target Market(s)

Families of children with special needs and medical colleagues.

Industry/Entity Type

Business

Requirements
Must have
• Include logo and pertinent information.

```html
<!DOCTYPE html>
<html lang="en">
<head>
<meta charset="utf-8">
<title>Crossing Paths – Business Card</title>
<link rel="stylesheet" href="https://fonts.googleapis.com/css2?family=Nunito:wght@800;900&family=Open+Sans:wght@400;600&display=swap">
<style>
  :root {
    --page: #e9eaec;
    --card: #ffffff;
    --red: #e94b26;
    --blue: #1aa3d4;
    --green: #3cc02c;
    --yellow: #f3b81f;
    --ink: #2b2b2b;
  }
  * { box-sizing: border-box; margin: 0; padding: 0; }
  html, body { width: 1200px; height: 800px; overflow: hidden; }
  body {
    background: var(--page);
    display: flex;
    align-items: center;
    justify-content: center;
    gap: 40px;
    font-family: "Open Sans", sans-serif;
  }
  .card {
    position: relative;
    width: 530px;
    height: 303px;
    background: var(--card);
    box-shadow: 0 6px 20px rgba(0,0,0,.15);
    overflow: hidden;
  }

  /* Back side */
  .card-back .swoosh { position: absolute; inset: 0; width: 100%; height: 100%; }
  .card-back .content {
    position: absolute;
    left: 48px;
    top: 58px;
  }
  .mood {
    font-family: "Nunito", sans-serif;
    font-weight: 800;
    font-size: 17px;
    line-height: 1.3;
    letter-spacing: .3px;
    margin-bottom: 12px;
  }
  .mood .red { color: var(--red); }
  .mood .blue { color: var(--blue); }
  .mood .yellow { color: var(--yellow); }
  .mood .green { color: var(--green); }
  .contact { list-style: none; }
  .contact li {
    display: flex;
    align-items: center;
    gap: 8px;
    font-size: 15px;
    color: var(--ink);
    line-height: 1.55;
  }
  .contact svg { width: 18px; height: 18px; flex: none; }

  /* Front side */
  .card-front {
    display: flex;
    flex-direction: column;
    align-items: center;
    justify-content: center;
    text-align: center;
  }
  .brand {
    display: flex;
    align-items: center;
    gap: 12px;
    margin-bottom: 16px;
  }
  .brand-dot {
    width: 30px; height: 30px;
    border-radius: 50%;
    background: var(--green);
  }
  .brand-name {
    font-family: "Nunito", sans-serif;
    font-weight: 900;
    font-size: 50px;
    color: var(--red);
    line-height: 1;
  }
  .service {
    font-family: "Nunito", sans-serif;
    font-weight: 900;
    font-size: 25px;
    color: var(--red);
    line-height: 1.1;
  }
  .tagline {
    font-family: "Nunito", sans-serif;
    font-weight: 800;
    font-size: 19px;
    color: var(--blue);
    margin-top: 2px;
  }
</style>
</head>
<body>

  <section class="card card-back">
    <svg class="swoosh" viewBox="0 0 530 303" preserveAspectRatio="none" aria-hidden="true">
      <path d="M330 303 C 390 220, 440 165, 530 130 L 530 145 C 450 180, 405 235, 355 303 Z" fill="var(--red)"/>
      <path d="M395 303 C 440 245, 480 205, 530 185 L 530 196 C 488 215, 452 252, 412 303 Z" fill="var(--blue)"/>
    </svg>
    <div class="content">
      <p class="mood">
        <span class="red">SIMPLE</span> , <span class="blue">WARM</span>, <span class="yellow">JOY-FILLED</span><br>
        <span class="green">ENGAGING</span> , <span class="red">BRIDGE OF HOPE FEEL</span>
      </p>
      <ul class="contact">
        <li>
          <svg viewBox="0 0 20 20"><path d="M10 2 1 10h3v8h5v-5h2v5h5v-8h3z" fill="var(--red)"/></svg>
          4417 W. Alder Street Pine Hollow, AR 72860
        </li>
        <li>
          <svg viewBox="0 0 20 20"><path d="M3 6c0-2 3-3 7-3s7 1 7 3v2h-4V6H7v2H3z M5 9h10l2 8H3z" fill="var(--blue)"/><circle cx="10" cy="13" r="2" fill="#fff"/></svg>
          501-555-0148
        </li>
        <li>
          <svg viewBox="0 0 20 20"><rect x="1" y="4" width="18" height="12" fill="var(--yellow)"/><path d="M1 4l9 7 9-7" fill="none" stroke="#fff" stroke-width="1.5"/></svg>
          hello@crossingpaths.com
        </li>
        <li>
          <svg viewBox="0 0 20 20"><circle cx="10" cy="10" r="8.5" fill="var(--green)"/><g fill="none" stroke="#fff" stroke-width="1"><ellipse cx="10" cy="10" rx="3.5" ry="8.5"/><path d="M1.5 10h17M3 6h14M3 14h14"/></g></svg>
          crossingpaths.com
        </li>
      </ul>
    </div>
  </section>

  <section class="card card-front">
    <div class="brand">
      <span class="brand-dot"></span>
      <span class="brand-name">Crossing Paths</span>
    </div>
    <p class="service">Pediatric Therapy Services</p>
    <p class="tagline">Engaging children - Empowering families</p>
  </section>

</body>
</html>
```